Create a standard e-mail template for market research invitations.
Please follow attached layout.
E-mail template must be fully coded and uploaded to mailchimp account and fully tested before sign off.
Logos are uploaded. Our website is www.meetkestrelpod.co.uk . Please stick to corporate image.
Example content:
Previous example attached. Happy with this style design or something a bit different, but must stick to layout style (html template 1 doc.) also attached. Template should allow for placement of similar content to given example and be text editable.
Main left hand side of header must be readable text and not downloadable image only to increase readership and improve look when arriving in inbox.
Thanks
Target Market(s)
General consumers
Industry/Entity Type
Market Research

```html
<!DOCTYPE html>
<html lang="en">
<head>
<meta charset="utf-8">
<title>Kestrelpod – Market Research Invitation</title>
<link href="https://fonts.googleapis.com/css2?family=Arimo:wght@400;700&display=swap" rel="stylesheet">
<style>
  :root{
    --sky:#e7f4fd;
    --green:#8fbc1b;
    --green-dark:#5b8a2d;
    --green-light:#97bb5c;
    --brown:#7b6f63;
    --brown-dark:#71665b;
    --text:#555555;
    --divider:#f3f3f3;
    --footer-dark:#666666;
    --white:#ffffff;
  }
  *{margin:0;padding:0;box-sizing:border-box;}
  html,body{width:970px;height:1200px;overflow:hidden;background:var(--sky);}
  body{font-family:"Arimo",Arial,sans-serif;color:var(--text);}
  .email{position:absolute;left:0;top:0;width:800px;height:990px;transform:scale(1.2125);transform-origin:0 0;}
  .abs{position:absolute;}
  a{color:inherit;}

  .preheader{left:0;width:800px;top:15px;text-align:center;font-size:14px;line-height:21px;}
  .preheader a{color:var(--text);}
  .sep{margin:0 10px;}

  .stripe{left:100px;top:70px;width:600px;height:10px;display:flex;}
  .stripe span{flex:1;background:var(--green);}
  .stripe span:nth-child(even){background:var(--brown);}

  .header{left:100px;top:80px;width:600px;height:160px;background:var(--white);}
  .headline{left:20px;top:36px;width:300px;font-size:27px;line-height:33px;font-weight:400;color:var(--brown);}
  .headline em{font-style:normal;color:var(--green);}
  .brand{left:332px;top:52px;display:flex;align-items:center;gap:10px;}
  .brand-dot{width:22px;height:22px;border-radius:50%;background:var(--green);}
  .brand-name{font-size:48px;font-weight:700;color:var(--green);letter-spacing:-1px;}

  .gap{left:100px;width:600px;height:10px;background:var(--divider);}

  .content{left:100px;top:250px;width:600px;height:600px;background:var(--white);}
  .bubbles{left:0;top:0;}
  .bubble-text{text-align:center;}
  .bubble-text h2{font-weight:700;}
  .bubble-text p{font-size:13.5px;line-height:21px;}
  .count{left:55px;top:72px;width:230px;color:var(--brown-dark);}
  .count h2{font-size:23px;line-height:25px;margin-bottom:8px;}
  .paid{left:312px;top:103px;width:220px;color:var(--white);}
  .paid h2{font-size:20px;line-height:24px;margin-bottom:9px;}

  .join{left:170px;top:350px;width:260px;height:48px;border:2px solid var(--green);border-radius:3px;
        display:flex;align-items:center;justify-content:center;font-size:19px;font-weight:700;color:var(--green);text-decoration:none;}

  .details{left:20px;top:429px;width:570px;}
  .details h3{font-size:17px;font-weight:700;color:var(--green);margin-bottom:9px;}
  .details p{font-size:14px;line-height:20px;margin-bottom:9px;}
  .benefits{list-style:none;font-size:14px;line-height:21px;}
  .benefits li{position:relative;padding-left:11px;}
  .benefits li::before{content:"";position:absolute;left:0;top:4px;width:6px;height:6px;border-radius:50%;background:var(--green);}

  .footer-links{left:100px;top:860px;width:600px;height:40px;background:var(--white);
        display:flex;align-items:center;justify-content:center;font-size:16px;color:var(--text);}
  .footer-links .sep{margin:0 11px;}
  .footer-links .green{color:var(--green);text-decoration:none;}
  .footer-legal{left:100px;top:900px;width:600px;height:40px;background:var(--footer-dark);color:var(--white);
        display:flex;align-items:center;justify-content:center;font-size:14px;}
  .footer-prefs{left:0;width:800px;top:953px;text-align:center;font-size:14px;}
  .footer-prefs a{color:var(--text);}
</style>
</head>
<body>
<div class="email">
  <div class="abs preheader">
    Is this email not displaying correctly?<br>
    <a href="#">View it in your browser</a><span class="sep">|</span><a href="#">Unsubscribe</a>
  </div>

  <div class="abs stripe"><span></span><span></span><span></span><span></span><span></span><span></span><span></span><span></span></div>

  <header class="abs header">
    <h1 class="abs headline">Make waves with your opinions <em>and get paid for it!</em></h1>
    <div class="abs brand"><span class="brand-dot"></span><span class="brand-name">kestrelpod</span></div>
  </header>

  <div class="abs gap" style="top:240px"></div>

  <main class="abs content">
    <svg class="abs bubbles" width="600" height="340" viewBox="0 0 600 340">
      <defs>
        <linearGradient id="greenFill" x1="0" y1="0" x2="1" y2="1">
          <stop offset="0" stop-color="#9cc064"/>
          <stop offset="1" stop-color="#54832a"/>
        </linearGradient>
        <filter id="soft" x="-20%" y="-20%" width="140%" height="140%">
          <feDropShadow dx="2" dy="4" stdDeviation="4" flood-color="#000" flood-opacity="0.25"/>
        </filter>
      </defs>
      <circle cx="170" cy="150" r="126" fill="#fff" stroke="#756a5f" stroke-width="4" filter="url(#soft)"/>
      <circle cx="422" cy="190" r="130" fill="url(#greenFill)" stroke="#fff" stroke-width="2" filter="url(#soft)"/>
    </svg>

    <div class="abs bubble-text count">
      <h2>Make your<br>opinions count!</h2>
      <p>Want to let the big brands know what you really think?<br>Sign up for paid market research studies and have your say!</p>
    </div>
    <div class="abs bubble-text paid">
      <h2>get paid for<br>your opinion...</h2>
      <p>We are always looking for people who are interested in giving their opinion on new products and services. Make waves with your views and get paid for it!</p>
    </div>

    <a class="abs join" href="#">Join Now</a>

    <section class="abs details">
      <h3>Get paid for your beautiful opinions!</h3>
      <p>Health and beauty companies need your expert opinions...</p>
      <ul class="benefits">
        <li>Invitations to participate in focus groups, telephone interviews and online surveys.</li>
        <li>Earn up to $100 for an hour of your time.</li>
        <li>Give your views on how companies innovate, launch, package and price their products.</li>
        <li>There is no cost to register and your privacy is guaranteed.</li>
      </ul>
    </section>
  </main>

  <div class="abs gap" style="top:850px"></div>

  <footer>
    <div class="abs footer-links">
      FAQ<span class="sep">|</span>01632 960481<span class="sep">|</span><a class="green" href="#">info@meetkestrelpod.co.uk</a><span class="sep">|</span><a class="green" href="#">Chatter</a><span class="sep">|</span><a class="green" href="#">Circles</a>
    </div>
    <div class="abs footer-legal">© 2013 Kestrelpod Ltd Kestrelpod Ltd, Harrow House, Linden Parade, Wexbury, WX4 2QB</div>
    <div class="abs footer-prefs">
      <a href="#">unsubscribe from this list</a><span class="sep">|</span><a href="#">update subscription preferences</a>
    </div>
  </footer>
</div>
</body>
</html>
```